Insurance company needs a business card design

We need a business card design for a Massachusetts-based insurance company Veloria Insurance, LLC. We provide auto insurance to Hispanic (Spanish- or Portuguese-speaking) immigrants in the United States. We will give these business cards to auto dealers where such customers typically go to purchase vehicles. We will provide a solution to the dealers to provide easy insurance to the customers buying cars at their dealerships. Veloria is the Spanish word for protection.
Contact Information for Business Card
Name, Designation, Company Name, Address, Phone Number, Email, Website
Look and feel
Each slider illustrates characteristics of the customer's brand and the style your logo design should communicate.

```html
<!DOCTYPE html>
<html lang="en">
<head>
<meta charset="utf-8">
<title>Veloria Insurance – Business Card</title>
<link rel="stylesheet" href="https://fonts.googleapis.com/css2?family=Arimo:wght@400;700&display=swap">
<style>
  :root {
    --navy: #17477f;
    --orange: #f08a1c;
    --ink: #2b2b2b;
    --paper: #ffffff;
    --backdrop: #e8e9eb;
  }
  * { margin: 0; padding: 0; box-sizing: border-box; }
  html, body { width: 1200px; height: 900px; overflow: hidden; }
  body {
    background: var(--backdrop);
    font-family: "Arimo", Arial, sans-serif;
    color: var(--ink);
    display: flex;
    flex-direction: column;
    align-items: center;
    justify-content: center;
    gap: 40px;
  }
  .card {
    position: relative;
    width: 680px;
    height: 389px;
    background: var(--paper);
    box-shadow: 0 6px 18px rgba(0,0,0,0.12);
    overflow: hidden;
  }
  .brand {
    display: flex;
    align-items: center;
    gap: 14px;
    color: var(--navy);
    font-weight: 700;
    text-transform: uppercase;
    letter-spacing: 0.04em;
    white-space: nowrap;
  }
  .brand-dot {
    border-radius: 50%;
    background: var(--orange);
    flex: none;
  }
  .card-front .brand {
    position: absolute;
    left: 50%; top: 50%;
    transform: translate(-50%, -50%);
    font-size: 40px;
  }
  .card-front .brand-dot { width: 44px; height: 44px; }
  .card-back .brand {
    position: absolute;
    left: 330px; top: 82px;
    font-size: 24px;
  }
  .card-back .brand-dot { width: 28px; height: 28px; }
  .wave { position: absolute; inset: 0; width: 100%; height: 100%; }
  .contact {
    position: absolute;
    left: 46px; top: 118px;
    font-size: 14px;
    line-height: 1.45;
  }
  .contact-name {
    color: var(--orange);
    font-weight: 700;
    font-size: 19px;
    letter-spacing: 0.02em;
    text-transform: uppercase;
  }
  .contact-role { margin-bottom: 6px; }
  .contact-address { margin-bottom: 6px; }
  .contact-list { list-style: none; }
  .contact-list li { display: flex; align-items: center; gap: 8px; }
  .contact-list svg { width: 14px; height: 14px; flex: none; }
  .web-domain { color: var(--navy); }
</style>
</head>
<body>
  <section class="card card-front" aria-label="Business card front">
    <div class="brand"><span class="brand-dot"></span>Veloria Insurance</div>
  </section>

  <section class="card card-back" aria-label="Business card back">
    <svg class="wave" viewBox="0 0 680 389" preserveAspectRatio="none" aria-hidden="true">
      <path d="M0 389 L0 384 C200 390 330 362 430 304 C520 250 600 190 680 168 L680 389 Z" fill="var(--navy)"/>
      <path d="M0 372 C200 378 330 350 430 290 C520 236 600 175 680 150" fill="none" stroke="var(--orange)" stroke-width="5"/>
    </svg>

    <div class="brand"><span class="brand-dot"></span>Veloria Insurance</div>

    <div class="contact">
      <p class="contact-name">Dario Whitcombe</p>
      <p class="contact-role">Co-Founder</p>
      <p class="contact-address">Harbor Point 1280 Shore Rd<br>Norwell Quay Suite 310</p>
      <p>Veloria Insurance, LLC</p>
      <ul class="contact-list">
        <li>
          <svg viewBox="0 0 16 16" aria-hidden="true"><circle cx="8" cy="8" r="8" fill="var(--orange)"/><path d="M5.2 4.2l1.6 1.8-.8 1c.5 1.1 1.3 1.9 2.4 2.4l1-.8 1.8 1.6-1 1.4C7.5 11.4 4.6 8.5 4 5.3z" fill="#fff"/></svg>
          617-555-0142
        </li>
        <li>
          <svg viewBox="0 0 16 16" aria-hidden="true"><circle cx="8" cy="8" r="8" fill="var(--orange)"/><rect x="4" y="5" width="8" height="6" fill="#fff"/><path d="M4 5l4 3.2L12 5" fill="none" stroke="var(--orange)" stroke-width="1"/></svg>
          info@veloriainsurance.com
        </li>
        <li>
          <svg viewBox="0 0 16 16" aria-hidden="true"><circle cx="8" cy="8" r="8" fill="var(--orange)"/><circle cx="8" cy="8" r="4.2" fill="none" stroke="#fff" stroke-width="1"/><path d="M3.8 8h8.4M8 3.8c-2 2.4-2 6 0 8.4M8 3.8c2 2.4 2 6 0 8.4" fill="none" stroke="#fff" stroke-width="1"/></svg>
          <span>www.<span class="web-domain">veloriainsurance</span>.com</span>
        </li>
      </ul>
    </div>
  </section>
</body>
</html>
```